" Visitamos clientes importadores e vendemos nossos servicos. Eles nos fornecem a factura a qual desejam importar e nos tratamos de todo o processo de desalfandegamento da mercadoria ate o transporte e entrega no armazem dos nossos clientes. "

```html
<!DOCTYPE html>
<html lang="pt-BR">
<head>
<meta charset="UTF-8">
<title>Assinatura de e-mail</title>
<link href="https://fonts.googleapis.com/css2?family=Montserrat:wght@500;600;700&display=swap" rel="stylesheet">
<style>
  :root {
    --bg: #dddddd;
    --navy: #0e2a84;
    --grey-mark: #9b9b9b;
    --white: #ffffff;
  }
  * { margin: 0; padding: 0; box-sizing: border-box; }
  html, body { width: 1200px; height: 1200px; overflow: hidden; background: var(--bg); }
  .canvas { position: relative; width: 1200px; height: 1200px; font-family: "Montserrat", Arial, sans-serif; }
  .band {
    position: absolute; left: 336px; top: 485px; width: 797px; height: 278px;
    background: var(--navy); border-radius: 0 139px 139px 0;
  }
  .brand-disc {
    position: absolute; left: 103px; top: 480px; width: 312px; height: 312px;
    border-radius: 50%; background: var(--bg); border: 12px solid var(--navy);
    display: flex; align-items: center; justify-content: center;
  }
  .brand-name {
    color: var(--grey-mark); font-weight: 700; font-size: 32px; line-height: 1.15;
    text-align: center; letter-spacing: 1px;
  }
  .identity {
    position: absolute; left: 614px; top: 508px; padding-left: 15px;
    border-left: 5px solid var(--white); color: var(--white);
  }
  .identity .name { font-weight: 700; font-size: 30px; line-height: 36px; }
  .identity .role { font-weight: 500; font-size: 24px; line-height: 26px; }
  .contacts { position: absolute; left: 612px; top: 584px; list-style: none; color: var(--white); }
  .contacts li { display: flex; align-items: center; height: 38px; font-size: 27px; font-weight: 500; }
  .contacts svg { width: 28px; height: 28px; margin-right: 14px; flex: none; }
</style>
</head>
<body>
<div class="canvas">
  <div class="band"></div>
  <div class="brand-disc"><span class="brand-name">SUA<br>MARCA</span></div>

  <div class="identity">
    <div class="name">NOME E SOBRENOME</div>
    <div class="role">Cargo | Função</div>
  </div>

  <ul class="contacts">
    <li>
      <svg viewBox="0 0 24 24"><path fill="#fff" d="M6.6 10.8a15 15 0 0 0 6.6 6.6l2.2-2.2a1 1 0 0 1 1-.25 11.4 11.4 0 0 0 3.6.57 1 1 0 0 1 1 1V20a1 1 0 0 1-1 1A17 17 0 0 1 3 4a1 1 0 0 1 1-1h3.5a1 1 0 0 1 1 1c0 1.25.2 2.45.57 3.57a1 1 0 0 1-.25 1z"/></svg>
      (00) 0000-0000
    </li>
    <li>
      <svg viewBox="0 0 24 24"><circle cx="12" cy="12" r="9" fill="none" stroke="#fff" stroke-width="2.4"/></svg>
      (00) 0000-0000
    </li>
    <li>
      <svg viewBox="0 0 24 24"><rect x="3" y="5" width="18" height="14" rx="1.5" fill="#fff"/><path d="M3.5 6l8.5 7 8.5-7" fill="none" stroke="#0e2a84" stroke-width="1.8"/></svg>
      contato@exemplo.com
    </li>
    <li>
      <svg viewBox="0 0 24 24" fill="none" stroke="#fff" stroke-width="2"><circle cx="12" cy="12" r="9"/><ellipse cx="12" cy="12" rx="4" ry="9"/><path d="M3 12h18M4.5 7.5h15M4.5 16.5h15"/></svg>
      www.exemplo.com.br
    </li>
  </ul>
</div>
</body>
</html>
```